Wren Hollow Oils - Body Oils

I am in need of 4 different label and package designs for a new line of body oils that I am launching. I already have the logo and names, it is now a matter of positioning the content. The names are as follows;

1) CARDAMOM + CYPRESS
WARMING BODY OIL
2) NEROLI + LEMON
UPLIFTING BODY OIL
3) CEDAR + BIRCH
GROUNDING BODY OIL
4) SAGE + MINT
COOLING BODY OIL.
The size of each label is 13cm wide x 9.5cm high. The size of the box is 4.5cm x 4.5cm x 15.5cm high.
The size of the bottle is 4cm across the base and 10.5cm in glass height.
I have included an image from a line that I started to work on but it didn't go anywhere. I thought the borders looked good to frame it in however, I am not attached to anything at this point. I am also including a picture of a product line that has used different colors on the packaging. I am not certain that this is the direction I'd like to take however I like how it looks with them. If we were to add the color I think it should be JUST the boxes and NOT the labels and they would be as follows; WARMING OIL - warm burgundy, earth tones UPLIFTING OIL - warm light, lightish blues GROUNDING OIL - warm soft, brownish creams COOLING OIL - refreshing light, pale green possibly blue. I would be interested to see what adding a sprig of a plant would look like on the boxes however with the already busy logo it might look like too much is going on. As you will see in our instagram and website we currently have the bear logo in a foil. I am not sure that I want to proceed with this foil as it is difficult to photograph. I would like to look at colors that compliment the existing line of essential oils as well as the dark brown wood on the cap.
I have added a design that looks a bit industrial that I like, it reads black ops.

Target Market(s)

My market is mainly females who are interested in natural health age 17 - 70. There is a large movement for organic + green beauty. I would like the label to look and feel clean and natural. Something that has been wildcrafted, raw and completely from nature.

Industry/Entity Type

Health And Wellness

Colors

Designer to choose colors to be used in the design.

Requirements
Must have
• Appeal to very progressive organic consumers. Please see the pictures marked SAMPLES 1, 2, 3 + 4 for design ideas.
• Easy to read. Clean design.
• The following information should be on the label as well as the packaging box.
• Size - 100 ML
• Barcodes - still to come
• Ingredients:
• 1) CARDAMOM + CYPRESS WARMING BODY OIL - *Sunflower Oil, **Orange, **Cardamom, **Cypress, **Ginger *Organic, **Organic essential oil
• 2) NEROLI + LEMON UPLIFTING BODY OIL - *Sunflower oil, **Orange, **Neroli, **Grapefruit, **Lemon, **Bergamot, **Benzoin, *Organic, **Organic essential oil
• 3) CEDAR + BIRCH GROUNDING BODY OIL - *Sunflower Oil, **Cedarwood, **Birch, **Benzoin, **Patchouli,*Organic, **Organic essential oil
• 4) SAGE + MINT COOLING BODY OIL - *Sunflower oil, **Spearmint, **Clary Sage, **Geranium, **Ylang Ylang, *Organic, **Organic essential oil
• Suggested Use:
• Warm oil if desired. Apply to the full body after bathing, massage in motions toward the heart until the oil is mostly absorbed. Can also be added to bath water.
Nice to have
• I would like to see the designs on the actual bottle (pic included) to see how it looks.
Should not have
• Bright colors.

```html
<!DOCTYPE html>
<html lang="en">
<head>
<meta charset="utf-8">
<title>Wren Hollow Oils – Body Oil Labels</title>
<link href="https://fonts.googleapis.com/css2?family=Open+Sans:wght@400;600;700&display=swap" rel="stylesheet">
<style>
  :root {
    --page: #ffffff;
    --label: #f0f0f0;
    --ink: #2f3a44;
    --brand-grey: #9c9c9c;
    --dots: #3a3f45;
    --warming: #e65f56;
    --cooling: #9cc65a;
    --uplifting: #eda83e;
    --grounding: #b99167;
  }
  * { box-sizing: border-box; margin: 0; padding: 0; }
  html, body { width: 1200px; height: 830px; overflow: hidden; background: var(--page); }
  body { font-family: "Open Sans", Arial, sans-serif; color: var(--ink); }
  .label-row {
    position: absolute; left: 40px; top: 125px;
    display: flex; gap: 40px;
  }
  .label {
    position: relative; width: 250px; height: 580px;
    background: var(--label);
  }
  .brand-name {
    position: absolute; top: 78px; left: 0; width: 100%;
    text-align: center; font-size: 14px; font-weight: 700;
    color: var(--brand-grey); letter-spacing: 0.3px;
  }
  .oil-header { position: absolute; left: 0; top: 170px; width: 250px; height: 150px; }
  .oil-type { font-family: "Open Sans", Arial, sans-serif; font-size: 11px; letter-spacing: 1.2px; fill: var(--ink); }
  .dotted-arc { fill: none; stroke: var(--dots); stroke-width: 2.2; stroke-linecap: round; stroke-dasharray: 0 6; }
  .product-name {
    position: absolute; top: 333px; left: 0; width: 100%;
    text-align: center; font-size: 20px; line-height: 28px;
    letter-spacing: 2px; font-weight: 400;
  }
  .colour-band { position: absolute; left: 0; top: 400px; width: 100%; height: 162px; }
  .warming .colour-band { background: var(--warming); }
  .cooling .colour-band { background: var(--cooling); }
  .uplifting .colour-band { background: var(--uplifting); }
  .grounding .colour-band { background: var(--grounding); }
</style>
</head>
<body>
<svg width="0" height="0" style="position:absolute">
  <defs>
    <path id="type-arc" d="M 35 72 A 100 100 0 0 1 215 72"/>
    <linearGradient id="warming-tone" x1="0" x2="1"><stop offset="0" stop-color="#ee5a55"/><stop offset="0.5" stop-color="#f29a5a"/><stop offset="1" stop-color="#5e4436"/></linearGradient>
    <linearGradient id="cooling-tone" x1="0" y1="0" x2="0" y2="1"><stop offset="0" stop-color="#9ccc5a"/><stop offset="0.45" stop-color="#39a9dc"/><stop offset="1" stop-color="#3bb14a"/></linearGradient>
    <linearGradient id="uplifting-tone" x1="0" x2="1"><stop offset="0" stop-color="#f0b24a"/><stop offset="0.5" stop-color="#e2562b"/><stop offset="1" stop-color="#f0b24a"/></linearGradient>
    <linearGradient id="grounding-tone" x1="0" y1="0" x2="1" y2="1"><stop offset="0" stop-color="#4a2615"/><stop offset="1" stop-color="#a97e58"/></linearGradient>
  </defs>
</svg>

<main class="label-row">
  <section class="label warming">
    <p class="brand-name">Wren Hollow Oils</p>
    <svg class="oil-header" viewBox="0 0 250 150">
      <text class="oil-type"><textPath href="#type-arc" startOffset="50%" text-anchor="middle">WARMING BODY OIL</textPath></text>
      <path class="dotted-arc" d="M 38 78 A 100 100 0 0 0 25 119"/>
      <path class="dotted-arc" d="M 212 78 A 100 100 0 0 1 225 119"/>
      <rect role="img" aria-label="Fan of overlapping petals in warm red and brown tones" x="65" y="58" width="120" height="74" rx="37" fill="url(#warming-tone)"/>
    </svg>
    <h2 class="product-name">CARDAMON<br>&amp; CYPRESS</h2>
    <div class="colour-band"></div>
  </section>

  <section class="label cooling">
    <p class="brand-name">Wren Hollow Oils</p>
    <svg class="oil-header" viewBox="0 0 250 150">
      <text class="oil-type"><textPath href="#type-arc" startOffset="50%" text-anchor="middle">COOLING BODY OIL</textPath></text>
      <path class="dotted-arc" d="M 38 78 A 100 100 0 0 0 25 119"/>
      <path class="dotted-arc" d="M 212 78 A 100 100 0 0 1 225 119"/>
      <rect role="img" aria-label="Stack of balanced stones in green and blue" x="75" y="58" width="100" height="74" rx="34" fill="url(#cooling-tone)"/>
    </svg>
    <h2 class="product-name">SAGE<br>&amp; MINT</h2>
    <div class="colour-band"></div>
  </section>

  <section class="label uplifting">
    <p class="brand-name">Wren Hollow Oils</p>
    <svg class="oil-header" viewBox="0 0 250 150">
      <text class="oil-type"><textPath href="#type-arc" startOffset="50%" text-anchor="middle">UPLIFTING BODY OIL</textPath></text>
      <path class="dotted-arc" d="M 38 78 A 100 100 0 0 0 25 119"/>
      <path class="dotted-arc" d="M 212 78 A 100 100 0 0 1 225 119"/>
      <rect role="img" aria-label="Blossom of orange and red petals" x="65" y="58" width="120" height="74" rx="37" fill="url(#uplifting-tone)"/>
    </svg>
    <h2 class="product-name">NEROLI<br>&amp; LEMON</h2>
    <div class="colour-band"></div>
  </section>

  <section class="label grounding">
    <p class="brand-name">Wren Hollow Oils</p>
    <svg class="oil-header" viewBox="0 0 250 150">
      <text class="oil-type"><textPath href="#type-arc" startOffset="50%" text-anchor="middle">GROUNDING BODY OIL</textPath></text>
      <path class="dotted-arc" d="M 38 78 A 100 100 0 0 0 25 119"/>
      <path class="dotted-arc" d="M 212 78 A 100 100 0 0 1 225 119"/>
      <rect role="img" aria-label="Overlapping earth-brown stones" x="70" y="58" width="110" height="74" rx="36" fill="url(#grounding-tone)"/>
    </svg>
    <h2 class="product-name">CEDAR<br>&amp; BIRCH</h2>
    <div class="colour-band"></div>
  </section>
</main>
</body>
</html>
```